Buchcover-Design für Science-Fiction-Roman
Zielgruppe
Ich habe einen Science-Fiction-Roman geschrieben und benötige dafür ein Buchcover.
Meine Zielgruppe sind Leser- und Leserinnen ab 18, Science-Fiction-Fans.
Aufgabenstellung
Zur Einstimmung und Orientierung habe ich ein kurzes Exposé und eine Leseprobe des Romans hochgeladen.
Für das Cover stelle ich mir etwas Dezentes aber trotzdem künstlerisch Anspruchsvolles vor, gerne auch abstrakt.
Es sollte der Titel (Unter Glas), meine Name (Lenor Vasić) und 'Roman' auf dem Cover.
Den genauen Klappentext reiche ich noch nach.
Das Format ist 12,7 x 20,32 cm (5 x 8 Zoll), Rückenbreite etwa 2 cm.

```html
<!DOCTYPE html>
<html lang="de">
<head>
<meta charset="utf-8">
<title>Unter Glas – Buchumschlag</title>
<link rel="stylesheet" href="https://fonts.googleapis.com/css2?family=Poiret+One&family=Roboto+Slab:wght@400&display=swap">
<style>
  :root {
    --ink: #000000;
    --paper: #ffffff;
    --glove-dark: #111111;
    --glove-light: #6a6a6a;
  }
  html, body {
    margin: 0;
    padding: 0;
    overflow: hidden;
    background: var(--ink);
  }
  .cover {
    position: relative;
    width: 1200px;
    height: 886px;
    overflow: hidden;
    background: var(--ink);
  }
  .cover__paper {
    position: absolute;
    inset: 0;
  }
  .back-blurb {
    position: absolute;
    left: 104px;
    top: 196px;
    width: 410px;
    margin: 0;
    font-family: "Roboto Slab", serif;
    font-size: 15px;
    line-height: 21.5px;
    color: var(--ink);
    hyphens: auto;
    -webkit-hyphens: auto;
  }
  .back-blurb p {
    margin: 0 0 21.5px;
  }
  .spine {
    position: absolute;
    left: 552px;
    top: -2px;
    width: 90px;
    height: 890px;
    box-sizing: border-box;
    border: 1.5px solid var(--ink);
    background: var(--paper);
  }
  .spine__author,
  .spine__title {
    position: absolute;
    left: 50%;
    font-family: "Poiret One", sans-serif;
    line-height: 1;
    color: var(--ink);
    white-space: nowrap;
    transform: translate(-50%, -50%) rotate(90deg);
    letter-spacing: 1px;
  }
  .spine__author {
    top: 244px;
    font-size: 30px;
  }
  .spine__title {
    top: 692px;
    font-size: 40px;
  }
  .front-author {
    position: absolute;
    left: 784px;
    top: 34px;
    width: 300px;
    text-align: center;
    white-space: nowrap;
    font-family: "Poiret One", sans-serif;
    font-size: 38px;
    letter-spacing: 1px;
    color: var(--ink);
  }
  .front-title {
    position: absolute;
    left: 660px;
    top: 160px;
    width: 520px;
    margin: 0;
    text-align: center;
    white-space: nowrap;
    font-family: "Poiret One", sans-serif;
    font-weight: 400;
    font-size: 78px;
    line-height: 1.1;
    letter-spacing: 2px;
    color: var(--ink);
  }
  .front-genre {
    position: absolute;
    left: 854px;
    top: 286px;
    width: 140px;
    text-align: center;
    white-space: nowrap;
    font-family: "Poiret One", sans-serif;
    font-size: 28px;
    line-height: 1;
    color: var(--ink);
  }
  .front-artwork {
    position: absolute;
    left: 838px;
    top: 342px;
    width: 182px;
    height: 482px;
    border-radius: 56px 56px 18px 18px;
    background: linear-gradient(160deg, var(--glove-light), var(--glove-dark) 55%, var(--ink));
  }
</style>
</head>
<body>
<div class="cover">
  <svg class="cover__paper" width="1200" height="886" viewBox="0 0 1200 886" aria-hidden="true">
    <path fill="#ffffff" d="M70 78 L180 58 L300 30 L420 12 L556 0 L556 886 L420 878 L300 870 L170 858 L72 838 L66 700 L60 500 L64 300 Z"/>
    <path fill="#ffffff" d="M640 0 L1125 0 L1150 40 L1185 95 L1190 300 L1185 560 L1180 760 L1150 820 L1100 850 L900 880 L640 886 Z"/>
  </svg>

  <div class="back-blurb">
    <p>Als Ina ihren Freund Jim aus einem Fenster eines siebenstöckigen Bürogebäudes fallen sieht, betätigt sie den „Zeitstopper“. Jim bleibt in der Luft hängen. Unter ihm befindet sich ein Bürgersteig mit unzähligen Passanten, auf die er fallen und mit in den Tod reißen könnte.</p>
    <p>Ina versucht nun buchstäblich in Lichtgeschwindigkeit einen Weg zu finden, Jim und die Passanten zu retten. Eine scheinbar unmögliche Aufgabe steht ihr bevor, die sie mental, physisch und emotional fordern wird.</p>
  </div>

  <div class="spine">
    <span class="spine__author">LENOR VASIĆ</span>
    <span class="spine__title">UNTER GLAS</span>
  </div>

  <div class="front-author">LENOR VASIĆ</div>
  <h1 class="front-title">UNTER GLAS</h1>
  <div class="front-genre">ROMAN</div>
  <div class="front-artwork" role="img" aria-label="Schwarz-weiße Illustration einer erhobenen Hand in einem gepanzerten, mechanischen Handschuh"></div>
</div>
</body>
</html>
```